Velmorique needs a elegant mystical business card design

The theme of Velmorique is centered on Kemetic/Ancient Egyptian Spirituality. My business sells handmade scented candles, mystic oils, body sprays, tarot readings and more. I would like my business card to reflect an elegant and mystical look. Hieroglyphs around the borders would be a cool idea. Also, the main colors I am working with is Black and Gold= colors of royalty. Black background. The business card will be double sided. The back will have the logo, and the front will have the basic information (ie name, title, business, phone, email, website, etc..)

Target Market(s)

The target market are people into metaphysics, holistic healing, ancient Egyptian culture, aromatherapy, occult science, and the esoteric.

Industry/Entity Type

Business

Contact Information for Business Card

Name: Marlonda T. Pruitt
Title: Owner
Business: VELMORIQUE
Phone: 917.302.4417
Website: www.Velmorique.net
Facebook, Instagram, and twitter icons

Font styles to use
Serif
Decorative

Requirements
Must have
• My logo, and website.
Nice to have
• Ancient Egyptian hieroglyphs, Elegant designs around the border, or encircling the logo.

```html
<!DOCTYPE html>
<html lang="en">
<head>
<meta charset="utf-8">
<title>Velmorique — Business Card</title>
<link href="https://fonts.googleapis.com/css2?family=Open+Sans:wght@400;600;700&display=swap" rel="stylesheet">
<style>
  :root {
    --page: #e9e6e1;
    --card-black: #0b0908;
    --card-black-soft: #1c1815;
    --gold-light: #e2c9a3;
    --gold: #c9a574;
    --gold-deep: #a27a45;
    --ink: #1a1410;
    --ink-soft: #3a2e24;
  }
  * { margin: 0; padding: 0; box-sizing: border-box; }
  html, body {
    width: 1200px; height: 843px; overflow: hidden;
    background: var(--page);
    font-family: "Open Sans", Arial, sans-serif;
  }
  .sheet {
    width: 1200px; height: 843px;
    display: flex; flex-direction: column;
    align-items: center; justify-content: center; gap: 40px;
  }
  .card {
    position: relative;
    width: 640px; height: 366px;
    border-radius: 20px;
    overflow: hidden;
    background: linear-gradient(160deg, var(--card-black-soft) 0%, var(--card-black) 60%);
    box-shadow: 0 10px 28px rgba(0,0,0,0.28);
  }

  /* Back side */
  .back-pattern {
    position: absolute; inset: 0;
    background:
      linear-gradient(180deg, rgba(201,165,116,0.05) 0%, rgba(201,165,116,0.09) 50%, rgba(201,165,116,0.04) 100%);
  }
  .brand-lockup {
    position: absolute; left: 0; right: 0; top: 50%;
    transform: translateY(-50%);
    display: flex; align-items: center; justify-content: center; gap: 14px;
  }
  .brand-dot {
    width: 16px; height: 16px; border-radius: 50%;
    background: var(--gold);
  }
  .brand-name {
    color: var(--gold);
    font-weight: 600;
    letter-spacing: 0.08em;
    font-size: 40px;
  }

  /* Front side */
  .front-art { position: absolute; inset: 0; }
  .front-brand {
    position: absolute; right: 48px; top: 82px;
    display: flex; align-items: center; gap: 10px;
  }
  .front-brand .brand-name { font-size: 30px; }
  .front-brand .brand-dot { width: 12px; height: 12px; }

  .contact {
    position: absolute; left: 66px; top: 120px;
    color: var(--ink);
  }
  .contact-name { font-size: 24px; font-weight: 700; line-height: 1.1; }
  .contact-title { font-size: 15px; color: var(--ink-soft); margin: 4px 0 10px; }
  .contact-list { list-style: none; }
  .contact-list li {
    display: flex; align-items: center; gap: 10px;
    font-size: 16px; line-height: 1.5;
  }
  .contact-list svg { width: 14px; height: 14px; flex: none; }
</style>
</head>
<body>
  <main class="sheet">

    <section class="card card-back" aria-label="Card back">
      <div class="back-pattern" role="img" aria-label="Faint band of gold hieroglyphs across the card"></div>
      <div class="brand-lockup">
        <span class="brand-dot"></span>
        <span class="brand-name">VELMORIQUE</span>
      </div>
    </section>

    <section class="card card-front" aria-label="Card front">
      <svg class="front-art" viewBox="0 0 640 366" aria-hidden="true">
        <defs>
          <linearGradient id="goldDisc" x1="0" y1="0" x2="1" y2="1">
            <stop offset="0" stop-color="#e9d3b0"/>
            <stop offset="0.55" stop-color="#d0ad7d"/>
            <stop offset="1" stop-color="#a98150"/>
          </linearGradient>
        </defs>
        <circle cx="176" cy="262" r="232" fill="none" stroke="#000" stroke-width="10"/>
        <circle cx="164" cy="262" r="216" fill="url(#goldDisc)"/>
      </svg>

      <div class="contact">
        <p class="contact-name">Marlonda T. Pruitt</p>
        <p class="contact-title">Owner</p>
        <ul class="contact-list">
          <li>
            <svg viewBox="0 0 24 24"><path fill="#1a1410" d="M6.6 10.8a15.1 15.1 0 0 0 6.6 6.6l2.2-2.2a1 1 0 0 1 1-.25 11.4 11.4 0 0 0 3.6.57 1 1 0 0 1 1 1V20a1 1 0 0 1-1 1A17 17 0 0 1 3 4a1 1 0 0 1 1-1h3.5a1 1 0 0 1 1 1c0 1.25.2 2.45.57 3.57a1 1 0 0 1-.25 1z"/></svg>
            917.302.4417
          </li>
          <li>
            <svg viewBox="0 0 24 24"><rect x="2" y="5" width="20" height="14" rx="2" fill="#1a1410"/><path d="M3 6l9 7 9-7" fill="none" stroke="#d0ad7d" stroke-width="1.6"/></svg>
            info@Velmorique.net
          </li>
          <li>
            <svg viewBox="0 0 24 24"><circle cx="12" cy="12" r="10" fill="#1a1410"/><path d="M2 12h20M12 2c3 3 3 17 0 20M12 2c-3 3-3 17 0 20" fill="none" stroke="#d0ad7d" stroke-width="1.4"/></svg>
            www.Velmorique.net
          </li>
        </ul>
      </div>

      <div class="front-brand">
        <span class="brand-dot"></span>
        <span class="brand-name">VELMORIQUE</span>
      </div>
    </section>

  </main>
</body>
</html>
```